StayCrewly.com homepage

We need a new homepage for our new domain.

StayCrewly.com

The colors to be used are the ones in our logo (attached) and in the current log in page host.nestarloo.com

Its important its a ONE PAGE site where you can scroll and elements appear while scrolling down.

It has to be simple to the point similar to the chatterloop log in page.

The current log in box and registration box have to stay but can be moved around obviously.

Also the video as on our current page www.nestarloo.com needs to have its place on the homepage.

Slogan

StayCrewly.com - The Booking Collaboration Platform.

Vacation rental managers and hosts can now team up with a booking team. Its easy to instantly improve your online booking management. Be on all the best booking sites without all the hassle. Improve your current strategy and save loads of time which you can spend on the satisfaction of your guests.

Something like that not too long.

I look forward to seeing your proposed designs.

In the attachment is our logo and a screenshot of our backend so the design will match nicely

Target Market(s)

Owners and property managers of vacation rentals world wide

Industry/Entity Type

Domain

Number of Pages Required

1 page

Requirements
Nice to have
• Smooth scrolling elements

```html
<!DOCTYPE html>
<html lang="en">
<head>
<meta charset="utf-8">
<title>StayCrewly.com – The Booking Collaboration Platform</title>
<link rel="stylesheet" href="https://fonts.googleapis.com/css2?family=Raleway:wght@500;600;700&family=Roboto:wght@400;500&display=swap">
<style>
  :root {
    --orange: #e0501a;
    --orange-bright: #f05a1e;
    --blue: #1d4fa8;
    --dark: #1a1a1c;
    --ink: #ffffff;
  }
  * { box-sizing: border-box; margin: 0; padding: 0; }
  html, body { width: 742px; height: 1200px; overflow: hidden; }
  body { position: relative; background: var(--dark); font-family: "Roboto", sans-serif; color: var(--ink); }
  a { color: inherit; text-decoration: none; }
  .abs { position: absolute; }

  /* hero */
  .hero { left: 0; top: 0; width: 742px; height: 589px;
    background: linear-gradient(180deg, #1f2835 0%, #2b3340 35%, #4a4643 65%, #5a5048 100%); }
  .header-rule { left: 0; top: 51px; width: 742px; height: 1px; background: rgba(255,255,255,.35); }
  .brand-mark { left: 44px; top: 26px; width: 12px; height: 12px; background: var(--orange-bright); }
  .brand-name { left: 63px; top: 22px; font: 700 17px/20px "Raleway", sans-serif; color: #fff; }
  .nav-item { display: block; top: 0; height: 51px; font: 500 7px/56px "Roboto", sans-serif; letter-spacing: .2px; }
  .nav-item.active { background: var(--orange); padding: 0 8px; }
  .call { left: 642px; top: 16px; font: 500 7px/10px "Roboto", sans-serif; }
  .call .label { color: var(--orange-bright); }
  .call .num { font-size: 8.5px; }
  .call-icon { left: 622px; top: 19px; }

  .community-title { font: 600 24px/30px "Raleway", sans-serif; }
  .community-lines { font: 400 10.5px/15.5px "Roboto", sans-serif; }
  .btn { display: block; text-align: center; font: 500 8px "Roboto", sans-serif; text-transform: uppercase; color: #fff; }
  .btn-host { left: 212px; top: 307px; width: 116px; height: 27px; line-height: 27px; background: var(--blue); }
  .btn-guest { left: 398px; top: 311px; width: 116px; height: 27px; line-height: 27px; background: var(--orange-bright); }

  .feature-rule { left: 0; top: 475px; width: 742px; height: 1px; background: rgba(255,255,255,.8); }
  .feature { width: 76px; height: 76px; border-radius: 50%; border: 2px solid #fff; background: var(--orange);
    display: flex; align-items: center; justify-content: center; }
  .feature.light { background: #fff; }
  .feature-label { font: 600 10px "Raleway", sans-serif; color: var(--orange-bright); letter-spacing: .3px; text-align: center; width: 130px; }
  .dot { top: 566px; width: 7px; height: 7px; border-radius: 50%; background: #fff; }
  .dot.on { background: var(--orange); }

  /* social band */
  .band { left: 0; top: 589px; width: 742px; height: 179px;
    background: linear-gradient(100deg, #2f6bc8 0%, #2460be 55%, #3a73c9 100%); }
  .band-title { left: 81px; top: 619px; font: 600 18px "Raleway", sans-serif; }
  .band-copy { left: 85px; top: 652px; width: 360px; font-size: 7.4px; line-height: 14px; }
  .btn-view { left: 81px; top: 726px; width: 94px; height: 23px; line-height: 23px; background: var(--orange); font-size: 9px; }

  /* services */
  .services-title { left: 0; top: 794px; width: 742px; text-align: center; font: 600 21px "Raleway", sans-serif; }
  .services-title span { color: var(--orange-bright); }
  .services-copy { left: 67px; top: 835px; width: 610px; text-align: center; font-size: 7px; line-height: 13px; }
  .card-image { top: 881px; width: 212px; height: 121px; }
  .card-title { top: 1013px; width: 212px; font: 500 10.5px/14.5px "Roboto", sans-serif; }
  .card-title.orange { color: var(--orange-bright); }
  .card-title.blue { color: #3f7ad8; }
  .card-copy { top: 1047px; width: 212px; font-size: 7px; line-height: 10.5px; }
  .btn-more { top: 1088px; width: 62px; height: 22px; line-height: 20px; font-size: 7px; border: 1px solid #fff; }
  .btn-more.orange { background: var(--orange); }
  .btn-more.blue { background: var(--blue); }

  .footer { left: 0; top: 1149px; width: 742px; height: 51px; background: var(--orange); }
  .footer-text { left: 30px; top: 1171px; font-size: 7.5px; }
  .social-dot { top: 1171px; width: 9px; height: 9px; border-radius: 50%; background: rgba(255,255,255,.85); }
</style>
</head>
<body>

<!-- Hero -->
<section class="abs hero" role="img" aria-label="City skyline photograph seen from a hillside park at dusk"></section>
<div class="abs header-rule"></div>

<span class="abs brand-mark"></span>
<div class="abs brand-name">StayCrewly.com</div>

<nav>
  <a class="abs nav-item active" style="left:322px">FOR WHO?</a>
  <a class="abs nav-item" style="left:391px">TEAM UP</a>
  <a class="abs nav-item" style="left:446px">THE TOOLS</a>
  <a class="abs nav-item" style="left:507px">PRICING</a>
</nav>

<svg class="abs call-icon" width="14" height="14" viewBox="0 0 14 14">
  <path d="M3 1l2 3-1.3 1.3a8 8 0 0 0 5 5L10 9l3 2-1 2.2C6 13.5.5 8 .8 2z" fill="var(--orange-bright)"/>
</svg>
<div class="abs call"><div class="label">CALL US</div><div class="num">(+31)-20 555 0147</div></div>

<svg class="abs" style="left:24px;top:242px" width="16" height="58" viewBox="0 0 16 58">
  <polyline points="14,1 2,29 14,57" fill="none" stroke="#fff" stroke-width="1.3"/>
</svg>
<svg class="abs" style="left:700px;top:242px" width="16" height="58" viewBox="0 0 16 58">
  <polyline points="2,1 14,29 2,57" fill="none" stroke="#fff" stroke-width="1.3"/>
</svg>

<h1 class="abs community-title" style="right:409px;top:212px">Hosting Community</h1>
<p class="abs community-lines" style="right:414px;top:248px;text-align:right">Improve your guest experience<br>Booking team collaboration platform<br>Connect with local hosts and property managers</p>
<a class="abs btn btn-host">Host signup / login</a>

<h1 class="abs community-title" style="left:397px;top:215px">Guest Community</h1>
<p class="abs community-lines" style="left:397px;top:251px">Speedy Guest attention<br>Best price guaranteed direct bookings<br>Great services, discounts, add-ons and Travel insurance</p>
<a class="abs btn btn-guest">Guest signup / login</a>

<div class="abs feature-rule"></div>
<div class="abs feature light" style="left:68px;top:437px">
  <svg width="34" height="38" viewBox="0 0 34 38"><path d="M3 4h28L17 20z M17 20v14 M9 35h16" fill="none" stroke="#222" stroke-width="2.2"/><circle cx="24" cy="8" r="2" fill="#222"/></svg>
</div>
<div class="abs feature" style="left:243px;top:437px">
  <svg width="40" height="36" viewBox="0 0 40 36"><g fill="none" stroke="#fff" stroke-width="1.8"><path d="M4 34h32M6 34V16h28v18M12 34v-9h5v9M23 34v-9h5v9M13 16a7 7 0 0 1 14 0M6 16V6M34 16V6"/></g></svg>
</div>
<div class="abs feature" style="left:424px;top:437px">
  <svg width="40" height="38" viewBox="0 0 40 38"><g fill="none" stroke="#fff" stroke-width="2"><path d="M20 34c2-8 2-16-2-24"/><path d="M18 10c-4-4-10-4-14 0M18 10c4-5 10-5 16-1M18 10c-1-5 2-8 6-8"/><path d="M6 35h28"/></g></svg>
</div>
<div class="abs feature" style="left:596px;top:437px">
  <svg width="38" height="36" viewBox="0 0 38 36"><g fill="#fff"><path d="M6 34V10l12-6v30z"/><path d="M20 34V14h12v20z"/></g><g fill="var(--orange)"><rect x="9" y="13" width="3" height="3"/><rect x="13" y="13" width="3" height="3"/><rect x="9" y="19" width="3" height="3"/><rect x="13" y="19" width="3" height="3"/><rect x="23" y="18" width="3" height="3"/><rect x="27" y="18" width="3" height="3"/><rect x="23" y="24" width="3" height="3"/><rect x="27" y="24" width="3" height="3"/></g></svg>
</div>
<div class="abs feature-label" style="left:43px;top:527px">NIGHT LIFE</div>
<div class="abs feature-label" style="left:213px;top:529px">EVENTS &amp; TICKETS</div>
<div class="abs feature-label" style="left:401px;top:529px">BEST SPOTS</div>
<div class="abs feature-label" style="left:576px;top:525px">GETTING AROUND</div>

<div class="abs dot" style="left:364px"></div>
<div class="abs dot on" style="left:379px"></div>
<div class="abs dot" style="left:394px"></div>

<!-- Social booking band -->
<section class="abs band" role="img" aria-label="Blue tinted photograph of hands holding a tablet"></section>
<h2 class="abs band-title">The First Social Booking Network</h2>
<p class="abs band-copy">Lorem ipsum dolor sit amet, consectetur adipiscing elit, sed do eiusmod tempor incididunt ut labore et dolore magna aliqua. Ut enim ad minim veniam, quis nostrud exercitation ullamco laboris nisi ut aliquip ex ea commodo consequat.  culpa qui officia deserunt</p>
<a class="abs btn btn-view">VIEW ALL</a>
<svg class="abs" style="left:478px;top:664px" width="54" height="54" viewBox="0 0 54 54">
  <circle cx="27" cy="27" r="24" fill="none" stroke="#4a5a70" stroke-width="3.5"/>
  <path d="M21 16l16 11-16 11z" fill="#4a5a70"/>
</svg>

<!-- Services -->
<h2 class="abs services-title">Our <span>Service</span></h2>
<p class="abs services-copy">Lorem ipsum dolor sit amet, consectetur adipiscing elit, sed do eiusmod tempor incididunt ut labore et dolore magna aliqua. Ut enim ad minim veniam, quis nostrud exercitation ullam-co laboris. Duis aute irure dolor in reprehenderit in voluptate velit esse cillum dolore eu fugiat nulla pariatur.</p>

<div class="abs card-image" style="left:30px;background:linear-gradient(135deg,#e9ecef,#b9c2cc)" role="img" aria-label="Photograph of business colleagues discussing a booking plan"></div>
<div class="abs card-image" style="left:266px;background:linear-gradient(135deg,#5a5a5a,#d7d7d7)" role="img" aria-label="Photograph of a hand holding a smartphone showing the platform"></div>
<div class="abs card-image" style="left:503px;background:linear-gradient(135deg,#7a5c40,#3f9b3a)" role="img" aria-label="Photograph of a laptop and tablet on a wooden desk showing the platform"></div>

<h3 class="abs card-title orange" style="left:30px">Your Personal Booking Team handles nearly everything</h3>
<h3 class="abs card-title blue" style="left:266px;top:1015px">Connect to your Network From Anywhere</h3>
<h3 class="abs card-title blue" style="left:503px">Stay ahead with the best VR tools known to Nestarkind</h3>

<p class="abs card-copy" style="left:30px">Lorem ipsum dolor sit amet, consectetur adipiscing elit, sed do eiusmod tempor incididunt ut labore et dolore magna aliqua. Ut enim ad minim veniam, quis nostrud exercitation</p>
<p class="abs card-copy" style="left:266px;top:1049px">Lorem ipsum dolor sit amet, consectetur adipiscing elit, sed do eiusmod tempor incididunt ut labore et dolore magna aliqua. Ut enim ad minim veniam, quis nostrud exercitation</p>
<p class="abs card-copy" style="left:503px;top:1048px">Lorem ipsum dolor sit amet, consectetur adipiscing elit, sed do eiusmod tempor incididunt ut labore et dolore magna aliqua. Ut enim ad minim veniam, quis nostrud exercitation</p>

<a class="abs btn btn-more orange" style="left:30px">READ MORE</a>
<a class="abs btn btn-more blue" style="left:267px;top:1086px">READ MORE</a>
<a class="abs btn btn-more blue" style="left:504px;top:1087px">READ MORE</a>

<!-- Footer -->
<footer class="abs footer"></footer>
<div class="abs footer-text">All Rights Reserved. Copyrights @Company Name .2015</div>
<span class="abs social-dot" style="left:603px"></span>
<span class="abs social-dot" style="left:627px"></span>
<span class="abs social-dot" style="left:651px"></span>
<span class="abs social-dot" style="left:674px"></span>
<span class="abs social-dot" style="left:697px"></span>

</body>
</html>
```